Tourism Marketing needing sleek, clear design for business card & proposal documents.

***Company background***
"Quiet Harbour" is a company specializing in tourism marketing and project management. We do international wholesale, event management as well as ongoing representation of tourism and hospitality companies.

***Target market***
We cater to tourism companies and hotel professionals.

***Task***
We would like to get a single sided business card designed (but will still consider two sided, we are open to any ideas you may have). The layout for this card should be modern and elegant. Currently we do not have a logo, but we would like our business name in a really simple typography for the business card (similar to Moonrise Palace's logo - www.moonrisepalace-example.com.au).We are after a design that is clear, strong enough to be recognised as Quiet Harbour that does not require any fancy design. Another option is a simple play on QH (Quiet Harbour) or simply have Quiet Harbour featured elsewhere on card more as a brand/logo.

Feel free to submit different fonts if you feel you have any other fonts/designs that may be suitable for this card other than sans serifs. Should this project be successful, we will be considering several other projects for business proposal templates and eventually a website design.

The information that needs to go on the card are as follows:

Marta Holloway
Director
Quiet Harbour
Tourism Marketing & Representation
87 Wendover Parade
Larkfield, Victoria, 3188 Australia
T +61 498203617 E marta@quietharbour-example.com.au

***Look and feel***
We'd like the business card design to express the following:
Modern, sleek, elegant, simple, discreet, quality, subtle, professional, creative, innovation

In terms of typography, we like something really simple and blocky (similar font to Moonrise Palace's logo - www.moonrisepalace-example.com.au)

***Colour scheme***
Shades of grey and dark teal

***Note***
Although our main target market are professionals, we would like the business card design to be versatile enough to be used outside of the tourism industry and need to appeal to different markets.

I do not have existing logo. Was hoping for a design that may be clear, strong enough not to require one. Other option is a simple play on QH (Quiet Harbour) or simply have Quiet Harbour featured elsewhere on card more as a brand/logo.

Marta Holloway
Director
Quiet Harbour Pty Ltd 
87 Wendover Parade
T +61 498203617  E  marta@quietharbour-example.com.au

Thank you for designs so far. Many have used a mauve colour which matches our company profile. This is not necessary, as that is just a draft and will be completely redesigned, so dont  feel you need to incorporate the mauve.

My colour preferences are for a white or grey background, and I like fonts in dark teals, grey or other sophisticated but modern colours. feel free to submit different fonts if you you have other fonts you thing would be suitable for this card, along with sans serifs. Should this project be successful, we will be considering several others for business proposal templates and eventually website. 

Target Market(s)

International Hospitality Senior Executives, Directors of International Tourism Companies, Directors of Tourism Bodies Internationally, local Tourism

Industry/Entity Type

Hospitality

Requirements
Should not have
• must not have bright garish colour, swirly patterns or anything that dates too much.

```html
<!DOCTYPE html>
<html lang="en">
<head>
<meta charset="utf-8">
<title>Quiet Harbour — Business Card</title>
<link rel="stylesheet" href="https://fonts.googleapis.com/css2?family=Montserrat:wght@800&family=Barlow:wght@400;500&display=swap">
<style>
  :root {
    --backdrop: #eeeeee;
    --card: #333334;
    --ink: #ffffff;
    --ink-soft: #e6e6e6;
    --teal: #5e9f9c;
  }
  * { box-sizing: border-box; margin: 0; padding: 0; }
  html, body { width: 1200px; height: 848px; overflow: hidden; }
  body {
    background: var(--backdrop);
    display: flex;
    align-items: center;
    justify-content: center;
    gap: 60px;
    font-family: "Barlow", sans-serif;
    color: var(--ink);
  }
  .card {
    position: relative;
    width: 520px;
    height: 318px;
    background: var(--card);
    box-shadow: 0 2px 6px rgba(0,0,0,0.25);
  }
  .wordmark {
    display: flex;
    align-items: center;
    gap: 10px;
    font-family: "Montserrat", sans-serif;
    font-weight: 800;
    text-transform: uppercase;
    letter-spacing: 0.04em;
    color: var(--ink);
    white-space: nowrap;
  }
  .wordmark-dot {
    flex: none;
    border-radius: 50%;
    background: var(--teal);
  }
  .card-front .wordmark {
    position: absolute;
    left: 36px;
    top: 56px;
    font-size: 36px;
  }
  .card-front .wordmark-dot { width: 24px; height: 24px; }
  .tagline {
    position: absolute;
    left: 38px;
    top: 108px;
    font-size: 17px;
    letter-spacing: 0.05em;
    color: var(--ink-soft);
  }
  .person {
    position: absolute;
    left: 38px;
    top: 178px;
  }
  .person-name { font-size: 18px; font-weight: 500; }
  .person-role { font-size: 16px; color: var(--ink-soft); margin-top: 2px; }
  .contact {
    position: absolute;
    right: 30px;
    top: 178px;
    text-align: right;
    font-size: 12.5px;
    font-style: normal;
    line-height: 1.45;
    color: var(--ink-soft);
  }
  .card-back {
    display: flex;
    align-items: center;
    justify-content: center;
  }
  .card-back .wordmark { font-size: 24px; gap: 8px; }
  .card-back .wordmark-dot { width: 16px; height: 16px; }
</style>
</head>
<body>
  <section class="card card-front" aria-label="Business card front">
    <div class="wordmark"><span class="wordmark-dot"></span>Quiet Harbour</div>
    <p class="tagline">Tourism Marketing &amp; Representation</p>
    <div class="person">
      <p class="person-name">Marta Holloway</p>
      <p class="person-role">Director</p>
    </div>
    <address class="contact">
      87 Wendover Parade<br>
      Larkfield, Victoria, 3188 Australia<br>
      t. +61 498203617<br>
      e. marta@quietharbour-example.com.au
    </address>
  </section>

  <section class="card card-back" aria-label="Business card back">
    <div class="wordmark"><span class="wordmark-dot"></span>Quiet Harbour</div>
  </section>
</body>
</html>
```